Luxury skin care/beauty salon needs a fresh wordpress website makeover

Today we have a wordpress site that has served us well, and we want to stay with wordpress, but we need a new up to date fresh look, with an inviting and enticing front, and look that just draws people in to book an appoint for luxury beauty treatment.

The salon consists of beautisian/skin specialint, a cosmetical nurse, and a doctor, - so top notch expertice within skin care and beauty treatment.

- The site should be integrated with Postwren (which we currently do not use.

- The site should further be able to "show prices for treatments" in a manner that matches the new website in style and layout, - we do show prices today via ex. the booking module from a vendor, but its done via iFrame

- booking needs to be very easy and intuitive, and the site needs to be response, since 75% of our customers use Ipad or mobile phone while booking

- the colours of the logo and style for the company today is primarily gold and black, and the shop is kept in a minimalistic style

- we have fresh newly made professional pictures made, and we can also later supply a video for ex. a landing page

- we have a license for Framewick if that can be utilized

- we need to be able to translate all elements into minimum Norwegian

- we use QL and Snapvale today to promote our services, if that can be incorporated, that would be a promotion plus

today we have the following pages
- main page
- a treatment page, where treatments are in more detail explained, this also doubles as pricelist ... we might look to discard this, since its manually updated and is not the master ... the master is the booking system, which also contains princes
- a portfolio page, seperated into types of treatments, this page also has one element of Snapvale which is one of the prime social media channals.
- a team member page, that presents the staff
- a contact us page
- a booking page ( that uses the national available booking system that we want to keep, but present in a different manner if possible) .. including gift card

we are not nessesarily looking to keep all pages, if the new design comes up with a more proffesional and smoother look, so this is debatable, so i have left the "How many web pages do you need designed?" to 4 pages .. again debatable

The final design should communicate luxury and professional skincare and beauty treatments, and easy booking.

Target Market(s)

Women or men that want to book a beauty or skin care treatment

Industry/Entity Type

Beauty and skin care salon

Coding

Coded - Design and coding required

Number of Pages Required

4 page

Colors

Designer to choose colors to be used in the design.

Requirements
Must have
• booking system, a connection to postwren, ability to change wording/language (Norwegian)
Nice to have
• video background, if it compliments the design
Should not have
• a new booking platform, we want to stick with the one we have

```html
<!DOCTYPE html>
<html lang="en">
<head>
<meta charset="utf-8">
<title>VELARA – Luxury Skincare &amp; Beauty Salon</title>
<link href="https://fonts.googleapis.com/css2?family=Poppins:wght@300;400;500;600;700;800&display=swap" rel="stylesheet">
<style>
:root{
  --gold:#e6b54a;
  --gold-soft:#f1d79a;
  --gold-pale:#f7ecd2;
  --ink:#111111;
  --text:#6b6b6b;
  --line:#e3c27a;
  --white:#ffffff;
}
*{box-sizing:border-box;margin:0;padding:0}
html,body{width:1200px;height:4389px;overflow:hidden}
body{position:relative;background:var(--white);font-family:'Poppins',sans-serif;color:var(--ink)}
.abs{position:absolute}
.photo{position:absolute}
.btn{position:absolute;background:var(--gold);color:var(--ink);font-weight:600;font-size:16px;display:flex;align-items:center;justify-content:center;letter-spacing:.3px}
.section-title{position:absolute;left:0;width:1200px;text-align:center;font-weight:800;font-size:38px;letter-spacing:.3px}
.circle-arrow{position:absolute;width:28px;height:28px;border:1.6px solid var(--ink);border-radius:50%;display:flex;align-items:center;justify-content:center}
.circle-arrow svg{width:12px;height:12px}

/* header */
.brand{position:absolute;left:94px;top:34px;width:238px;height:77px;display:flex;align-items:center;justify-content:center;font-weight:400;font-size:50px;letter-spacing:3px;line-height:1;color:var(--ink)}
.main-nav{position:absolute;left:397px;top:60px;display:flex;gap:33px;font-weight:600;font-size:17px}

/* hero */
.hero-gold{left:0;top:0;width:469px;height:702px;background:var(--gold)}
.hero-bg{left:469px;top:0;width:731px;height:702px;background:linear-gradient(135deg,#f7f6f3 0%,#efe8dc 55%,#f3ecdf 100%)}
.hero-model{left:100px;top:162px;width:420px;height:631px;background:linear-gradient(160deg,#f0d5bf 0%,#e9c3a6 60%,#f6f1ec 100%);border-radius:160px 120px 60px 160px}
.hero-title{left:500px;top:262px;width:666px;text-align:center;font-weight:800;font-size:60px;line-height:64px}
.hero-copy{left:560px;top:411px;width:546px;text-align:center;font-size:14px;line-height:18px;color:var(--text)}

/* welcome */
.welcome-copy{left:114px;top:991px;width:460px;font-size:12.5px;line-height:22.4px;color:var(--text)}
.checks{left:114px;top:1298px;width:380px;display:grid;grid-template-columns:166px 200px;row-gap:8px;font-size:13px;color:#333}
.checks li{list-style:none;display:flex;align-items:center;gap:10px}
.products{left:597px;top:972px;width:494px;height:460px;background:linear-gradient(180deg,#ffffff 0%,#eeeae4 60%,#e8d3a0 100%);border-radius:20px}

/* services */
.services-band{left:0;top:1568px;width:1200px;height:363px;background:var(--gold)}
.service-card{position:absolute;top:1733px;width:310px;height:440px;background:var(--white);box-shadow:0 4px 18px rgba(0,0,0,.08)}
.service-card h3{position:absolute;left:28px;top:38px;font-size:14.5px;font-weight:700}
.service-card .ico{position:absolute;right:30px;top:30px;width:36px;height:36px}
.service-card .rule{position:absolute;left:28px;right:28px;top:79px;border-top:1.5px solid var(--line)}
.service-card p{position:absolute;left:28px;top:100px;width:230px;font-size:13px;line-height:24px;color:var(--text)}
.service-card .time{position:absolute;left:24px;top:210px;font-size:12.5px;color:var(--text)}
.service-card .time b{color:var(--ink);font-weight:700}
.price-row{position:absolute;left:24px;right:28px;display:flex;align-items:center;font-size:12.5px;color:var(--text)}
.price-row b{color:var(--ink);font-weight:700;width:110px;line-height:17px}
.price-row .dash{flex:1;border-top:1.3px dashed #555;margin:0 10px}
.view-more{position:absolute;left:0;width:100%;top:394px;text-align:center;font-size:10px;font-weight:600;color:var(--gold)}
.view-more span{border-bottom:1px solid var(--gold);padding-bottom:2px}

/* clients */
.client-card{position:absolute;top:2349px;width:450px;height:242px;background:var(--white);box-shadow:0 4px 22px rgba(0,0,0,.08);padding:38px 24px}
.client-card p{font-size:13px;line-height:25px;color:var(--text)}
.client-meta{position:absolute;left:24px;top:152px;display:flex;align-items:center;gap:14px}
.avatar{width:50px;height:50px;border-radius:50%;background:linear-gradient(135deg,var(--gold-soft),var(--gold))}
.client-name{font-size:13px;font-weight:500}
.client-name small{font-size:12px;font-weight:400}
.stars{display:flex;gap:2px;margin-top:4px}
.quote-mark{position:absolute;right:30px;top:168px;font-size:44px;color:#e2e2e2;font-weight:800;line-height:1}

/* appointment */
.treat-photo{left:0;top:2697px;width:733px;height:675px;background:linear-gradient(120deg,#5b3d2c 0%,#a57556 35%,#e3c1a8 60%,#d9cfc9 100%)}
.treat-gold{left:733px;top:2697px;width:467px;height:675px;background:var(--gold)}
.booking-panel{left:327px;top:2770px;width:769px;height:528px;background:rgba(255,255,255,.9)}
.booking-panel h2{position:absolute;left:0;width:100%;top:62px;text-align:center;font-weight:800;font-size:38px}
.field{position:absolute;width:330px;height:60px;border:1.5px solid var(--gold-soft);background:var(--white);display:flex;align-items:center;justify-content:space-between;padding:0 20px 0 43px;font-size:15px;color:#333}

/* partners */
.partner-badge{position:absolute;top:3525px;width:259px;height:106px;border:2px solid var(--gold-soft);background:var(--white);display:flex;align-items:center;justify-content:center}
.partner-badge span{display:block;width:190px;height:34px;background:#e9e9e9;border-radius:4px}

/* newsletter + footer */
.dark-band{left:0;top:3866px;width:1200px;height:523px;background:var(--ink)}
.news-card{left:150px;top:3774px;width:900px;height:266px;background:var(--white);border-radius:14px;box-shadow:0 6px 24px rgba(0,0,0,.1)}
.duo-photo{left:179px;top:3682px;width:281px;height:361px;background:linear-gradient(170deg,#c28e6a 0%,#6d4a38 45%,#2b2a2a 100%);border-radius:120px 120px 0 0}
.news-copy{left:489px;top:3830px;width:520px;font-size:12.5px;line-height:25px;color:var(--text)}
.news-input{position:absolute;top:3971px;height:38px;border:1px solid #e5e5e5;display:flex;align-items:center;padding-left:14px;font-size:12.5px;color:#333;background:var(--white)}
.footer-brand{left:470px;top:4100px;width:260px;height:74px;display:flex;align-items:center;justify-content:center;color:var(--gold);font-size:50px;letter-spacing:3px;line-height:1;font-weight:400}
.footer-nav{left:0;top:4218px;width:1200px;display:flex;justify-content:center;gap:28px;color:var(--white);font-size:16px}
.social{position:absolute;top:4286px;width:27px;height:27px;border-radius:50%;background:var(--gold)}
.copyright{left:0;top:4348px;width:1200px;text-align:center;color:var(--white);font-size:16px}
.copy-line{position:absolute;top:4359px;height:1px;background:#ddd}
.deco{position:absolute;border-radius:50%;background:var(--gold-pale);opacity:.7}
</style>
</head>
<body>

<!-- Header -->
<div class="abs hero-gold"></div>
<div class="abs hero-bg" role="img" aria-label="Soft blurred backdrop of skincare cream jars"></div>
<div class="photo hero-model" role="img" aria-label="Seated woman in white underwear, smiling, photographed for skincare"></div>
<div class="brand">VELARA</div>
<nav class="main-nav"><span>HOME</span><span>ABOUT US</span><span>PORTFOLIO</span><span>OUR TEAM</span><span>OUR SERVICES</span><span>BOOKING</span></nav>

<!-- Hero -->
<h1 class="abs hero-title">LUXURY SKINCARE &amp;<br>BEAUTY SALON</h1>
<p class="abs hero-copy">Lorem Ipsum is simply dummy text of the printing and typesetting industry. Lorem Ipsum has been the industry's standard dummy text ever since the 1500s, when an unknown printer took a galley of type and</p>
<div class="btn" style="left:704px;top:494px;width:262px;height:51px">BOOK AN APPOINMENT</div>
<div class="circle-arrow" style="left:1068px;top:630px"><svg viewBox="0 0 12 12"><path d="M8 2 4 6l4 4" fill="none" stroke="#111" stroke-width="1.6"/></svg></div>
<div class="circle-arrow" style="left:1111px;top:630px"><svg viewBox="0 0 12 12"><path d="M4 2l4 4-4 4" fill="none" stroke="#111" stroke-width="1.6"/></svg></div>
<div class="deco" style="left:1083px;top:762px;width:74px;height:82px" role="img" aria-label="Faint line drawing of a face mask"></div>

<!-- Welcome -->
<h2 class="section-title" style="top:872px">WELCOME TO VELARA</h2>
<div class="abs welcome-copy">
  <p>Lorem Ipsum is simply dummy text of the printing and typesetting industry. Lorem Ipsum has been the industry's standard dummy text ever since the 1500s, when an unknown printer took a galley of type and scrambled it to make a type specimen book. It has survived not only five centuries, but also the leap into electronic typesetting, remaining essentially unchanged. It was popularised in the 1960s with the release of Letraset sheets containing Lorem Ipsum passages, and more recently with desktop publishing software like Aldus PageMaker including versions of Lorem Ipsum.</p>
  <p style="margin-top:14px">Lorem Ipsum is simply dummy text of the printing and typesetting</p>
</div>
<ul class="abs checks">
  <li><svg width="16" height="16" viewBox="0 0 16 16"><rect x="1" y="3" width="11" height="11" fill="none" stroke="#111" stroke-width="1.4"/><path d="M4 8l3 3 8-9" fill="none" stroke="#111" stroke-width="1.6"/></svg>Beautisian</li>
  <li><svg width="16" height="16" viewBox="0 0 16 16"><rect x="1" y="3" width="11" height="11" fill="none" stroke="#111" stroke-width="1.4"/><path d="M4 8l3 3 8-9" fill="none" stroke="#111" stroke-width="1.6"/></svg>Skin Specialist</li>
  <li><svg width="16" height="16" viewBox="0 0 16 16"><rect x="1" y="3" width="11" height="11" fill="none" stroke="#111" stroke-width="1.4"/><path d="M4 8l3 3 8-9" fill="none" stroke="#111" stroke-width="1.6"/></svg>Doctor</li>
  <li><svg width="16" height="16" viewBox="0 0 16 16"><rect x="1" y="3" width="11" height="11" fill="none" stroke="#111" stroke-width="1.4"/><path d="M4 8l3 3 8-9" fill="none" stroke="#111" stroke-width="1.6"/></svg>Cosmetical Nurse</li>
</ul>
<div class="btn" style="left:114px;top:1381px;width:137px;height:42px">READ MORE</div>
<div class="photo products" role="img" aria-label="White and gold branded cream tubes, jars and lipstick"></div>
<div class="deco" style="left:16px;top:1424px;width:86px;height:136px;border-radius:40px" role="img" aria-label="Faint line drawing of flowing hair"></div>

<!-- Services -->
<div class="abs services-band"></div>
<h2 class="section-title" style="top:1632px">OUR SERVICES</h2>
<div class="circle-arrow" style="left:1026px;top:1679px"><svg viewBox="0 0 12 12"><path d="M8 2 4 6l4 4" fill="none" stroke="#111" stroke-width="1.6"/></svg></div>
<div class="circle-arrow" style="left:1067px;top:1679px"><svg viewBox="0 0 12 12"><path d="M4 2l4 4-4 4" fill="none" stroke="#111" stroke-width="1.6"/></svg></div>

<article class="service-card" style="left:104px">
  <h3>MAKEUP FILTER</h3>
  <svg class="ico" viewBox="0 0 36 36"><path d="M6 14l20 16M10 8l20 16M14 4l16 14" fill="none" stroke="#333" stroke-width="2"/></svg>
  <div class="rule"></div>
  <p>It is a long established fact that a reader will be distracted by the readable content of a page when looking at its layout.</p>
  <div class="time"><b>Real Time :</b>&nbsp;&nbsp; 35 – 45 Mins</div>
  <div class="price-row" style="top:243px"><b>Bridal Makeup</b><span class="dash"></span>1200Kr</div>
  <div class="price-row" style="top:277px"><b>Bridal Makeup incl. Fiancé</b><span class="dash"></span>1700Kr</div>
  <div class="price-row" style="top:330px"><b>Makeup for a special occasion</b><span class="dash"></span>500Kr</div>
  <div class="view-more"><span>VIEW MORE &nbsp; →</span></div>
</article>

<article class="service-card" style="left:447px">
  <h3>EYE BAG REMOVAL</h3>
  <svg class="ico" viewBox="0 0 36 36"><path d="M3 16q15-12 30 0M6 20q12 8 24 0M10 23l-2 4M18 25v4M26 23l2 4" fill="none" stroke="#333" stroke-width="2"/></svg>
  <div class="rule"></div>
  <p>It is a long established fact that a reader will be distracted by the readable content of a page when looking at its layout.</p>
  <div class="time"><b>Real Time :</b>&nbsp;&nbsp; 15 – 25 Mins</div>
  <div class="price-row" style="top:251px"><b>Manscaping</b><span class="dash"></span>150Kr</div>
  <div class="price-row" style="top:285px"><b>Coloring Of Eye Lashes</b><span class="dash"></span>250Kr</div>
  <div class="price-row" style="top:338px"><b>Brow Styling</b><span class="dash"></span>390Kr</div>
  <div class="view-more"><span>VIEW MORE &nbsp; →</span></div>
</article>

<article class="service-card" style="left:788px">
  <h3>FACIAL TREATMENT</h3>
  <svg class="ico" viewBox="0 0 36 36"><circle cx="18" cy="16" r="9" fill="none" stroke="#333" stroke-width="2"/><path d="M7 33q11-8 22 0" fill="none" stroke="#333" stroke-width="2"/></svg>
  <div class="rule"></div>
  <p>It is a long established fact that a reader will be distracted by the readable content of a page when looking at its layout.</p>
  <div class="time"><b>Real Time :</b>&nbsp;&nbsp; 15 – 25 Mins</div>
  <div class="price-row" style="top:251px"><b>Consultation</b><span class="dash"></span>150Kr</div>
  <div class="price-row" style="top:283px"><b>Velara skin60</b><span class="dash"></span>990Kr</div>
  <div class="price-row" style="top:314px"><b>Velara skin30</b><span class="dash"></span>590Kr</div>
  <div class="price-row" style="top:345px"><b>Velara Ung</b><span class="dash"></span>700Kr</div>
  <div class="view-more"><span>VIEW MORE &nbsp; →</span></div>
</article>

<!-- Clients -->
<h2 class="section-title" style="top:2256px">OUR HAPPY CLIENTS</h2>
<div class="deco" style="left:1031px;top:2224px;width:162px;height:98px" role="img" aria-label="Faint line drawing of an open cream jar"></div>
<div class="circle-arrow" style="left:54px;top:2456px"><svg viewBox="0 0 12 12"><path d="M8 2 4 6l4 4" fill="none" stroke="#111" stroke-width="1.6"/></svg></div>
<div class="circle-arrow" style="left:1119px;top:2456px"><svg viewBox="0 0 12 12"><path d="M4 2l4 4-4 4" fill="none" stroke="#111" stroke-width="1.6"/></svg></div>

<article class="client-card" style="left:128px">
  <p>Lorem Ipsum is simply dummy text of the printing and typesetting industry. Lorem Ipsum has been the industry's standard dummy text ever since the 1500s, when an unknown printer took a galley of type and scrambled it to</p>
  <div class="client-meta">
    <div class="avatar" role="img" aria-label="Client portrait"></div>
    <div><div class="client-name">MAREN HOLT, <small>Position Name</small></div>
      <div class="stars">
        <svg width="17" height="17" viewBox="0 0 24 24"><path d="M12 2l3 7h7l-5.5 4.5 2 7.5L12 17l-6.5 4 2-7.5L2 9h7z" fill="#e6b54a"/></svg>
        <svg width="17" height="17" viewBox="0 0 24 24"><path d="M12 2l3 7h7l-5.5 4.5 2 7.5L12 17l-6.5 4 2-7.5L2 9h7z" fill="#e6b54a"/></svg>
        <svg width="17" height="17" viewBox="0 0 24 24"><path d="M12 2l3 7h7l-5.5 4.5 2 7.5L12 17l-6.5 4 2-7.5L2 9h7z" fill="#e6b54a"/></svg>
        <svg width="17" height="17" viewBox="0 0 24 24"><path d="M12 2l3 7h7l-5.5 4.5 2 7.5L12 17l-6.5 4 2-7.5L2 9h7z" fill="#e6b54a"/></svg>
        <svg width="17" height="17" viewBox="0 0 24 24"><path d="M12 2l3 7h7l-5.5 4.5 2 7.5L12 17l-6.5 4 2-7.5L2 9h7z" fill="none" stroke="#e6b54a" stroke-width="1.6"/></svg>
      </div></div>
  </div>
  <div class="quote-mark">”</div>
</article>

<article class="client-card" style="left:624px">
  <p>Lorem Ipsum is simply dummy text of the printing and typesetting industry. Lorem Ipsum has been the industry's standard dummy text ever since the 1500s, when an unknown printer took a galley of type and scrambled it to</p>
  <div class="client-meta">
    <div class="avatar" role="img" aria-label="Client portrait"></div>
    <div><div class="client-name">INGRID SOLLI, <small>Position Name</small></div>
      <div class="stars">
        <svg width="17" height="17" viewBox="0 0 24 24"><path d="M12 2l3 7h7l-5.5 4.5 2 7.5L12 17l-6.5 4 2-7.5L2 9h7z" fill="#e6b54a"/></svg>
        <svg width="17" height="17" viewBox="0 0 24 24"><path d="M12 2l3 7h7l-5.5 4.5 2 7.5L12 17l-6.5 4 2-7.5L2 9h7z" fill="#e6b54a"/></svg>
        <svg width="17" height="17" viewBox="0 0 24 24"><path d="M12 2l3 7h7l-5.5 4.5 2 7.5L12 17l-6.5 4 2-7.5L2 9h7z" fill="#e6b54a"/></svg>
        <svg width="17" height="17" viewBox="0 0 24 24"><path d="M12 2l3 7h7l-5.5 4.5 2 7.5L12 17l-6.5 4 2-7.5L2 9h7z" fill="#e6b54a"/></svg>
        <svg width="17" height="17" viewBox="0 0 24 24"><path d="M12 2l3 7h7l-5.5 4.5 2 7.5L12 17l-6.5 4 2-7.5L2 9h7z" fill="none" stroke="#e6b54a" stroke-width="1.6"/></svg>
      </div></div>
  </div>
  <div class="quote-mark">”</div>
</article>

<!-- Appointment -->
<div class="photo treat-photo" role="img" aria-label="Woman with long wavy brown hair having makeup brushed on"></div>
<div class="abs treat-gold"></div>
<form class="abs booking-panel">
  <h2>LUXURY BEAUTY TREATMENT</h2>
  <div class="field" style="left:45px;top:164px">First Name</div>
  <div class="field" style="left:396px;top:164px">Last Name</div>
  <div class="field" style="left:45px;top:247px">Contact Number</div>
  <div class="field" style="left:396px;top:247px">Email Address</div>
  <div class="field" style="left:45px;top:329px">Select An Date
    <svg width="22" height="22" viewBox="0 0 22 22"><rect x="2" y="4" width="18" height="16" fill="none" stroke="#333" stroke-width="1.6"/><path d="M2 9h18M7 2v4M15 2v4M6 12h2M10 12h2M14 12h2M6 16h2M10 16h2M14 16h2" stroke="#333" stroke-width="1.6"/></svg></div>
  <div class="field" style="left:396px;top:329px">Select A Time
    <svg width="22" height="22" viewBox="0 0 22 22"><circle cx="11" cy="11" r="9" fill="none" stroke="#333" stroke-width="1.8"/><path d="M11 6v5l3 3" fill="none" stroke="#333" stroke-width="1.8"/></svg></div>
  <div class="btn" style="left:218px;top:417px;width:331px;height:45px">MAKE AN APPOINMENT</div>
</form>

<!-- Partners -->
<h2 class="section-title" style="top:3449px">OUR SUPPORTED PARTNERS</h2>
<div class="deco" style="left:1012px;top:3406px;width:118px;height:82px" role="img" aria-label="Faint line drawing of a soap bar with bubbles"></div>
<div class="partner-badge" style="left:309px" role="img" aria-label="Partner badge"><span></span></div>
<div class="partner-badge" style="left:632px" role="img" aria-label="Partner badge"><span></span></div>

<!-- Newsletter -->
<div class="abs dark-band" role="img" aria-label="Dark backdrop with salon tools"></div>
<div class="deco" style="left:26px;top:3750px;width:68px;height:111px;border-radius:14px" role="img" aria-label="Faint line drawing of a serum dropper bottle"></div>
<div class="abs news-card"></div>
<div class="photo duo-photo" role="img" aria-label="Two smiling salon staff in black shirts"></div>
<div class="abs" style="left:476px;top:3796px;font-size:40px;color:#e2e2e2;font-weight:800;line-height:1">“</div>
<p class="abs news-copy">Lorem Ipsum is simply dummy text of the printing and typesetting industry. Lorem Ipsum has been the industry's standard dummy text ever since the 1500s, when an unknown printer took a galley of type and scrambled it to make a type specimen book. It has survived not only five</p>
<div class="abs" style="left:980px;top:3924px;font-size:40px;color:#e2e2e2;font-weight:800;line-height:1">”</div>
<div class="news-input" style="left:479px;width:169px">Full Name</div>
<div class="news-input" style="left:661px;width:200px">Email Address*</div>
<div class="btn" style="left:876px;top:3971px;width:131px;height:38px;font-size:13px;color:var(--white)">SUBSCRIBE</div>

<!-- Footer -->
<div class="abs footer-brand">VELARA</div>
<nav class="abs footer-nav">
  <span>HOME</span><span>|</span><span>ABOUT US</span><span>|</span><span>PORTFOLIO</span><span>|</span><span>OUR TEAM</span><span>|</span><span>OUR SERVICES</span><span>|</span><span>BOOKING</span>
</nav>
<div class="social" style="left:522px" aria-label="Social link"></div>
<div class="social" style="left:566px" aria-label="Social link"></div>
<div class="social" style="left:609px" aria-label="Social link"></div>
<div class="social" style="left:652px" aria-label="Social link"></div>
<div class="copy-line" style="left:106px;width:308px"></div>
<div class="copy-line" style="left:787px;width:308px"></div>
<div class="abs copyright">Copyright © 2021 Velara. All Rights Reserved.</div>

</body>
</html>
```